Overview of User Roles and their Functions

I need an overview of user roles and their functions. It should be presented on a A4 page to be shown during customer visits, but also put into our company presentation if possible.
I made a drawing with the information which needs to be mentioned (if it is not properly readable, please let me know)
The user roles are for our webportal Vendra-x Hub. To explain briefly: a producer can upload documents, and share them with distributors, who can use the same system to share documents with their customers. But a producer can also share documents directly with customers.
If you find a possibility to show these connections, may be with a document flying over to the right places, please try to implement this thought. Or additionally for the function: generate customer notification an email flying over to the distributor and customer. This could be flying over the top of the graph or underneath, or through it all, whatever works better without looking overloaded.
Producer and Distributor + are chargeable user accounts (you could add chargeable right underneath the title)
For the free distributor role I thought, this could all be slightly greyed out and have the Distributor + in more attractive colors. Producer and Customer can both be in attractive colors which stand out.
I tried to list the functions which are the same for different roles all on one line. May be you have a good idea about how not to let it look empty where there is no function mentioned?
Because I didn't have enough space, I didn't write docs properly as documents, or req.s as requests. Please choose a size where it is possible to write out the whole word.
as a background or generally, please use similar colors like on my website www.vendraxhub.example . To make something stand out, you can also use different colors.
Please let me know if you have any additional questions. I am happy to answer them...
Target Market(s)
Pharmaceutical
Industry/Entity Type
Pharmaceutical
Font styles to use
Other font styles liked:
- if it is possible please use Raleway but if with Raleway the overview or readability is bad, use your own selected
Requirements
Must have
- clear overview of functions but if somehow possible, also show the connection the user roles can have with each other

```html
<!DOCTYPE html>
<html lang="en">
<head>
<meta charset="utf-8">
<title>Cloud User Roles – Vendra-x Hub</title>
<link rel="stylesheet" href="https://fonts.googleapis.com/css2?family=Raleway:wght@700;800&family=Open+Sans:ital,wght@0,400;0,600;1,400&display=swap">
<style>
  :root{
    --page:#f2f3f4;
    --band:#0b4d98;
    --band-light:#1f73b8;
    --panel:#f5f5f5;
    --cell:#e8e8e8;
    --cell-alt:#ededed;
    --text:#3a3d42;
    --dash:#a3a6aa;
    --producer:#0b4f9e;
    --dist-free:#f08a1c;
    --dist-plus:#2aa3dc;
    --customer:#7cbf3c;
    --line:#8c9096;
  }
  *{box-sizing:border-box;margin:0;padding:0}
  html,body{width:1200px;height:887px;overflow:hidden;background:var(--page)}
  body{position:relative;font-family:"Open Sans",Arial,sans-serif;color:var(--text)}
  .backdrop{position:absolute;inset:0;width:1200px;height:887px}
  .title{position:absolute;left:84px;top:52px;font-family:"Raleway",Arial,sans-serif;font-weight:800;font-size:68px;letter-spacing:0.5px;color:var(--producer);line-height:1}
  .website{position:absolute;left:92px;top:126px;font-size:30px;color:#2a2d33;letter-spacing:0.3px}
  .brand{position:absolute;left:902px;top:86px;display:flex;align-items:center;gap:10px}
  .brand-mark{width:34px;height:34px;border-radius:50%;background:var(--producer)}
  .brand-name{font-family:"Open Sans",Arial,sans-serif;font-weight:600;font-size:26px;color:var(--producer)}
  .panel{position:absolute;left:77px;top:315px;width:1044px;height:504px;background:var(--panel)}
  .role{position:absolute;top:268px;width:208px}
  .role--producer{left:95px;--accent:var(--producer)}
  .role--dist-free{left:361px;--accent:var(--dist-free)}
  .role--dist-plus{left:628px;--accent:var(--dist-plus)}
  .role--customer{left:895px;--accent:var(--customer)}
  .role-head{height:48px;border-radius:24px 24px 0 0;background:var(--accent);color:#fff;text-align:center;display:flex;flex-direction:column;justify-content:center;line-height:1}
  .role-name{font-family:"Open Sans",Arial,sans-serif;font-weight:600;font-size:20px}
  .role-note{font-size:9px;opacity:.85;margin-top:2px}
  .role-list{list-style:none;margin-top:2px}
  .fn{height:34px;margin-bottom:2px;background:var(--cell);display:flex;align-items:center;padding-left:12px;font-size:13px;line-height:1.1;color:var(--text)}
  .fn:nth-child(even){background:var(--cell-alt)}
  .fn svg{width:19px;height:19px;flex:none;margin-right:12px;color:var(--accent)}
  .fn--empty::after{content:"";flex:1;margin-right:12px;border-top:1px dashed var(--dash)}
  .fn small{display:block;font-size:7px;font-style:italic;margin-top:1px}
  .base-bar{position:absolute;left:95px;top:786px;width:1008px;height:16px;background:var(--producer)}
  .flows{position:absolute;inset:0;width:1200px;height:887px;pointer-events:none}
</style>
</head>
<body>

<svg class="backdrop" viewBox="0 0 1200 887" aria-hidden="true">
  <rect x="0" y="315" width="1200" height="572" fill="var(--band)"/>
  <polygon points="0,330 77,372 77,819 0,887" fill="var(--band-light)"/>
  <polygon points="0,887 77,819 420,819" fill="var(--band-light)"/>
  <polygon points="1121,640 1200,612 1200,887 1121,887" fill="#0d57a6"/>
</svg>

<svg width="0" height="0" style="position:absolute" aria-hidden="true">
  <defs>
    <symbol id="i-upload" viewBox="0 0 24 24"><path d="M7 17H6a4 4 0 0 1-.5-8A6 6 0 0 1 17 8a4 4 0 0 1 1 9h-1M12 20v-8m-3 3 3-3 3 3" fill="none" stroke="currentColor" stroke-width="1.6" stroke-linecap="round" stroke-linejoin="round"/></symbol>
    <symbol id="i-download" viewBox="0 0 24 24"><path d="M7 16H6a4 4 0 0 1-.5-8A6 6 0 0 1 17 7a4 4 0 0 1 1 9h-1M12 11v9m-3-3 3 3 3-3" fill="none" stroke="currentColor" stroke-width="1.6" stroke-linecap="round" stroke-linejoin="round"/></symbol>
    <symbol id="i-share" viewBox="0 0 24 24"><g fill="none" stroke="currentColor" stroke-width="1.6"><circle cx="18" cy="5" r="2.5"/><circle cx="6" cy="12" r="2.5"/><circle cx="18" cy="19" r="2.5"/><path d="m8.2 10.8 7.6-4.5M8.2 13.2l7.6 4.5"/></g></symbol>
    <symbol id="i-bell" viewBox="0 0 24 24"><path d="M6 16V11a6 6 0 0 1 12 0v5l2 2H4zM10 20a2 2 0 0 0 4 0" fill="none" stroke="currentColor" stroke-width="1.6" stroke-linejoin="round"/></symbol>
    <symbol id="i-inbox" viewBox="0 0 24 24"><g fill="none" stroke="currentColor" stroke-width="1.6"><rect x="4" y="3" width="16" height="18" rx="1"/><path d="M8 8h8M8 12h8M8 16h5"/></g></symbol>
    <symbol id="i-search" viewBox="0 0 24 24"><g fill="none" stroke="currentColor" stroke-width="1.8" stroke-linecap="round"><circle cx="10" cy="10" r="6"/><path d="m15 15 5 5"/></g></symbol>
    <symbol id="i-lock" viewBox="0 0 24 24"><g fill="none" stroke="currentColor" stroke-width="1.6"><rect x="5" y="10" width="14" height="11" rx="1"/><path d="M8 10V7a4 4 0 0 1 8 0v3M12 14v3"/></g></symbol>
    <symbol id="i-version" viewBox="0 0 24 24"><g fill="none" stroke="currentColor" stroke-width="1.6" stroke-linecap="round"><rect x="4" y="4" width="16" height="16" rx="1"/><path d="M8 16 16 8M11 8h5v5M8 11v5h5"/></g></symbol>
    <symbol id="i-check" viewBox="0 0 24 24"><g fill="none" stroke="currentColor" stroke-width="1.6" stroke-linecap="round" stroke-linejoin="round"><path d="M19 12v8H4V5h11"/><path d="m8 11 4 4 9-10"/></g></symbol>
    <symbol id="i-warning" viewBox="0 0 24 24"><g fill="none" stroke="currentColor" stroke-width="1.6" stroke-linejoin="round"><circle cx="6" cy="6" r="3"/><path d="M14 6 23 21H5zM14 12v4M14 18v1"/></g></symbol>
    <symbol id="i-report" viewBox="0 0 24 24"><g fill="none" stroke="currentColor" stroke-width="1.6"><path d="M6 3h9l4 4v14H6z"/><path d="M9 10h7M9 13h7M9 16h7"/></g></symbol>
    <symbol id="i-auto" viewBox="0 0 24 24"><g fill="none" stroke="currentColor" stroke-width="1.6"><path d="M5 3h10l4 4v14H5z"/><circle cx="12" cy="13" r="4"/><path d="M12 11v2l1.5 1.5"/></g></symbol>
    <symbol id="i-stamp" viewBox="0 0 24 24"><g fill="none" stroke="currentColor" stroke-width="1.6" stroke-linejoin="round"><path d="M9 3h6v6l-1 4h4l2 4H4l2-4h4L9 9z"/><path d="M4 21h16"/></g></symbol>
    <symbol id="i-mail" viewBox="0 0 24 18"><g fill="none" stroke="currentColor" stroke-width="1.6" stroke-linejoin="round"><rect x="1.5" y="1.5" width="21" height="15"/><path d="m1.5 1.5 10.5 8 10.5-8"/></g></symbol>
  </defs>
</svg>

<h1 class="title">CLOUD USER ROLES</h1>
<p class="website">www.vendraxhub.example</p>
<div class="brand"><span class="brand-mark"></span><span class="brand-name">Vendra-x Hub</span></div>

<div class="panel"></div>

<section class="role role--producer">
  <header class="role-head"><span class="role-name">Producer</span><span class="role-note">chargeable</span></header>
  <ul class="role-list">
    <li class="fn"><svg><use href="#i-upload"/></svg>Upload Documents</li>
    <li class="fn"><svg><use href="#i-share"/></svg>Share</li>
    <li class="fn fn--empty"></li>
    <li class="fn"><svg><use href="#i-upload"/></svg>Upload COAS</li>
    <li class="fn"><svg><use href="#i-bell"/></svg><span>Generate Customer<br>Notifications</span></li>
    <li class="fn fn--empty"></li>
    <li class="fn fn--empty"></li>
    <li class="fn"><svg><use href="#i-check"/></svg>Receive access requests</li>
    <li class="fn"><svg><use href="#i-version"/></svg><span>Versioning System<small>(View difference between old/new file)</small></span></li>
    <li class="fn"><svg><use href="#i-warning"/></svg>Expiry Notification</li>
    <li class="fn"><svg><use href="#i-report"/></svg>Reports</li>
    <li class="fn"><svg><use href="#i-auto"/></svg><span>Automated<br>emailed Reports</span></li>
    <li class="fn"><svg><use href="#i-stamp"/></svg>Set stamps on docs</li>
  </ul>
</section>

<section class="role role--dist-free">
  <header class="role-head"><span class="role-name">Distributor FREE</span></header>
  <ul class="role-list">
    <li class="fn fn--empty"></li>
    <li class="fn"><svg><use href="#i-share"/></svg>Share</li>
    <li class="fn"><svg><use href="#i-download"/></svg>Download Docs</li>
    <li class="fn fn--empty"></li>
    <li class="fn"></li>
    <li class="fn"><svg><use href="#i-inbox"/></svg>Receive Notifications</li>
    <li class="fn"><svg><use href="#i-search"/></svg><span>View other<br>Listed Supplies</span></li>
    <li class="fn"><svg><use href="#i-lock"/></svg>Request access</li>
    <li class="fn"><svg><use href="#i-version"/></svg>Versioning System</li>
    <li class="fn fn--empty"></li>
    <li class="fn fn--empty"></li>
    <li class="fn fn--empty"></li>
    <li class="fn fn--empty"></li>
  </ul>
</section>

<section class="role role--dist-plus">
  <header class="role-head"><span class="role-name">Distributor +</span><span class="role-note">chargeable</span></header>
  <ul class="role-list">
    <li class="fn"><svg><use href="#i-upload"/></svg>Upload Documents</li>
    <li class="fn"><svg><use href="#i-share"/></svg>Share</li>
    <li class="fn"><svg><use href="#i-download"/></svg>Download Docs</li>
    <li class="fn"></li>
    <li class="fn"><svg><use href="#i-bell"/></svg><span>Generate Customer<br>Notifications</span></li>
    <li class="fn"><svg><use href="#i-inbox"/></svg>Receive Notifications</li>
    <li class="fn"><svg><use href="#i-search"/></svg><span>View other<br>Listed Supplies</span></li>
    <li class="fn"><svg><use href="#i-lock"/></svg>Request access</li>
    <li class="fn"><svg><use href="#i-version"/></svg>Versioning System</li>
    <li class="fn"><svg><use href="#i-warning"/></svg>Expiry Notification</li>
    <li class="fn"><svg><use href="#i-report"/></svg>Reports</li>
    <li class="fn"><svg><use href="#i-auto"/></svg><span>Automated<br>emailed Reports</span></li>
    <li class="fn"><svg><use href="#i-stamp"/></svg>Set stamps on docs</li>
  </ul>
</section>

<section class="role role--customer">
  <header class="role-head"><span class="role-name">Custsomer FREE</span></header>
  <ul class="role-list">
    <li class="fn fn--empty"></li>
    <li class="fn fn--empty"></li>
    <li class="fn"><svg><use href="#i-download"/></svg>Download Docs</li>
    <li class="fn fn--empty"></li>
    <li class="fn fn--empty"></li>
    <li class="fn"><svg><use href="#i-inbox"/></svg>Receive Notifications</li>
    <li class="fn"><svg><use href="#i-search"/></svg><span>View other<br>Listed Supplies</span></li>
    <li class="fn"><svg><use href="#i-lock"/></svg>Request access</li>
    <li class="fn"><svg><use href="#i-version"/></svg>Versioning System</li>
    <li class="fn fn--empty"></li>
    <li class="fn fn--empty"></li>
    <li class="fn fn--empty"></li>
    <li class="fn fn--empty"></li>
  </ul>
</section>

<div class="base-bar"></div>

<svg class="flows" viewBox="0 0 1200 887" aria-label="Connections between user roles">
  <g fill="none" stroke="var(--line)" stroke-width="1.2" stroke-dasharray="3 3">
    <path d="M334 370V258Q334 240 352 240H848Q866 240 866 258V362Q866 370 874 370H892"/>
    <path d="M316 370H358M584 370H624M851 370H892"/>
    <path d="M316 478H594Q604 478 604 488V505Q604 515 614 515H624"/>
    <path d="M334 478V505Q334 515 344 515H358"/>
    <path d="M604 478V468Q604 458 614 458H856Q866 458 866 468V505Q866 515 876 515H892"/>
    <path d="M851 478H866"/>
  </g>
  <g fill="var(--customer)">
    <polygon points="580,233 592,240 580,247"/>
    <polygon points="596,233 608,240 596,247"/>
    <polygon points="612,233 624,240 612,247"/>
  </g>
  <polygon points="304,362 317,370 304,378" fill="var(--producer)"/>
  <polygon points="572,362 585,370 572,378" fill="var(--dist-free)"/>
  <polygon points="839,362 852,370 839,378" fill="var(--dist-plus)"/>
  <polygon points="304,470 317,478 304,486" fill="var(--producer)"/>
  <polygon points="839,470 852,478 839,486" fill="var(--dist-plus)"/>
  <circle cx="361" cy="370" r="4" fill="var(--dist-free)"/>
  <circle cx="627" cy="370" r="4" fill="var(--dist-plus)"/>
  <circle cx="895" cy="370" r="4" fill="var(--customer)"/>
  <circle cx="361" cy="515" r="4" fill="var(--dist-free)"/>
  <circle cx="627" cy="515" r="4" fill="var(--dist-plus)"/>
  <circle cx="895" cy="515" r="4" fill="var(--customer)"/>
  <svg x="318" y="494" width="19" height="14" style="color:var(--dist-free)"><use href="#i-mail"/></svg>
  <svg x="586" y="482" width="19" height="14" style="color:var(--dist-plus)"><use href="#i-mail"/></svg>
  <svg x="873" y="462" width="19" height="14" style="color:var(--customer)"><use href="#i-mail"/></svg>
</svg>

</body>
</html>
```